Business Cards

I'd like help creating business cards with the full logo "Veltrona Capital Partners" on the back of the card (navy background with white writing), and abbreviated logo "VCP" on the front. Would like to list name, title, phone number, email, and website listed on front of card. Would like to keep very simple. Front font Arial or similar.

```html
<!DOCTYPE html>
<html lang="en">
<head>
<meta charset="utf-8">
<title>Veltrona Capital Partners – Business Cards</title>
<link rel="stylesheet" href="https://fonts.googleapis.com/css2?family=Arimo:wght@400;700&family=Montserrat:wght@600;700&display=swap">
<style>
  :root {
    --navy: #1f3a6e;
    --white: #ffffff;
    --ink-grey: #6b6b6b;
    --page: #e9eaec;
  }
  * { box-sizing: border-box; margin: 0; padding: 0; }
  html, body { width: 1200px; height: 904px; overflow: hidden; }
  body {
    background: var(--page);
    font-family: "Arimo", Arial, sans-serif;
    display: flex;
    flex-direction: column;
    align-items: center;
    justify-content: center;
    gap: 48px;
  }
  .card {
    width: 620px;
    height: 354px;
    box-shadow: 0 6px 18px rgba(0,0,0,0.18);
    position: relative;
  }
  .card-back {
    background: var(--navy);
    display: flex;
    align-items: center;
    justify-content: center;
  }
  .wordmark-full {
    color: var(--white);
    font-family: "Montserrat", Arial, sans-serif;
    font-weight: 700;
    font-size: 34px;
    letter-spacing: 3px;
    text-transform: uppercase;
    text-align: center;
    line-height: 1.35;
  }
  .card-front { background: var(--white); }
  .contact-block {
    position: absolute;
    left: 56px;
    top: 112px;
  }
  .person-name {
    font-family: "Montserrat", Arial, sans-serif;
    font-weight: 700;
    font-size: 19px;
    color: var(--navy);
    letter-spacing: 0.5px;
    text-transform: uppercase;
  }
  .person-title {
    font-size: 16px;
    color: var(--ink-grey);
    margin-top: 4px;
  }
  .contact-list {
    list-style: none;
    margin-top: 20px;
  }
  .contact-list li {
    display: flex;
    align-items: center;
    gap: 8px;
    font-size: 17px;
    color: var(--ink-grey);
    line-height: 26px;
  }
  .contact-icon { width: 16px; height: 16px; flex: none; }
  .wordmark-short {
    position: absolute;
    right: 56px;
    top: 150px;
    display: flex;
    align-items: center;
    gap: 10px;
  }
  .wordmark-short-text {
    font-family: "Montserrat", Arial, sans-serif;
    font-weight: 700;
    font-size: 52px;
    color: var(--navy);
    letter-spacing: 2px;
  }
  .wordmark-short-square {
    width: 14px;
    height: 14px;
    background: var(--navy);
  }
</style>
</head>
<body>
  <section class="card card-back" aria-label="Card back">
    <p class="wordmark-full">Veltrona<br>Capital Partners</p>
  </section>

  <section class="card card-front" aria-label="Card front">
    <div class="contact-block">
      <h1 class="person-name">Delaney Hartwell</h1>
      <p class="person-title">Chief of Staff</p>
      <ul class="contact-list">
        <li>
          <svg class="contact-icon" viewBox="0 0 16 16" aria-hidden="true"><path fill="#1f3a6e" d="M3.5 1.5l2.5 3-1.6 1.6c.9 2 2.5 3.6 4.5 4.5L10.5 9l3 2.5-1.5 2.5C6.5 14 2 9.5 1.5 4z"/></svg>
          (555) 318-4720
        </li>
        <li>
          <svg class="contact-icon" viewBox="0 0 16 16" aria-hidden="true"><rect x="1.5" y="3.5" width="13" height="9" fill="none" stroke="#1f3a6e" stroke-width="1.5"/><path d="M1.5 3.5L8 9l6.5-5.5" fill="none" stroke="#1f3a6e" stroke-width="1.5"/></svg>
          Delaney.Hartwell@VeltronaCP.com
        </li>
        <li>
          <svg class="contact-icon" viewBox="0 0 16 16" aria-hidden="true"><g fill="none" stroke="#1f3a6e" stroke-width="1.3"><circle cx="8" cy="8" r="6.3"/><ellipse cx="8" cy="8" rx="2.8" ry="6.3"/><path d="M1.7 8h12.6M2.8 4.8h10.4M2.8 11.2h10.4"/></g></svg>
          www.VeltronaCP.co.uk
        </li>
      </ul>
    </div>
    <div class="wordmark-short">
      <span class="wordmark-short-text">VCP</span>
      <span class="wordmark-short-square" aria-hidden="true"></span>
    </div>
  </section>
</body>
</html>
```